Anzeigengestaltung für Wochenblatt
Zielgruppe
Wir bieten professionelle Schädlingsbekämpfung an. Unsere Zielgruppe sind Privathaushalte, aber auch Gewerbekunden mit Schädlingsproblemen. Zu den hauptsächlichen Schädlingen zählen Mäuse, Ratten, Wespen, Schaben, Silberfische, Ameisen sowie verschiedene weitere Insekten (Käfer, Fliegen usw.)
Aufgabenstellung
Es sollten verschiedene Vorlagen erstellt werden, da die Schädlinge je nach Jahreszeit auftreten. Im Frühjahr/Sommer sind es vermehrt Wespen, Ameisen und Insekten, im Herbst/Winter vermehrt Ratten/Mäuse
Für Wespen speziell hätten wir gerne eine Anzeige als "Wespen-Notruf" mit unserer Telefon-Nummer und der Internetadresse www.plagenfrei-team.example
Die Anzeige soll 1-oder 2-spaltig erscheinen und bunt sein. Die Höhe sollte nicht ins unendliche gehen, da jeder mm Geld kostet, hier sollten also die Informationen kurz und knapp dargelegt werden. Unser Logo sollte am unteren Rand enthalten sein.

```html
<!DOCTYPE html>
<html lang="de">
<head>
<meta charset="utf-8">
<title>Wespen-Alarm Anzeige</title>
<link rel="stylesheet" href="https://fonts.googleapis.com/css2?family=Alfa+Slab+One&family=Arimo:wght@700&display=swap">
<style>
  :root {
    --page: #ffffff;
    --alarm-yellow: #f9d319;
    --ink: #111111;
    --signal-red: #c8171b;
    --brand-green: #5a9a1e;
    --frame: #9a9a9a;
  }
  * { box-sizing: border-box; margin: 0; padding: 0; }
  html, body { width: 848px; height: 1200px; overflow: hidden; background: var(--page); }
  .canvas { position: relative; width: 848px; height: 1200px; }

  .ad {
    position: absolute; left: 309px; top: 211px;
    width: 178px; height: 445px;
    border: 1px solid var(--frame);
    background: var(--page);
    overflow: hidden;
    font-family: "Arimo", Arial, sans-serif;
  }
  .ad-field {
    position: absolute; inset: 0;
    width: 178px; height: 445px;
  }
  .headline {
    position: absolute; left: 0; top: 14px; width: 178px;
    text-align: center;
    font-family: "Alfa Slab One", Georgia, serif;
    font-size: 27px; line-height: 30px;
    color: var(--ink);
    letter-spacing: 1px;
  }
  .wasp-art {
    position: absolute; left: 38px; top: 86px;
    width: 110px; height: 150px;
    border-radius: 45% 45% 40% 40%;
    background: linear-gradient(180deg, #141414 0%, #141414 45%, #3a3200 60%, #141414 75%, #2b2500 100%);
  }
  .help-tag {
    position: absolute; left: 12px; top: 220px;
    width: 98px; height: 28px;
    background: var(--signal-red);
    color: #fff;
    border-radius: 5px;
    font-size: 13px; line-height: 28px;
    text-align: center;
    transform: rotate(-5deg);
  }
  .help-arrow { position: absolute; left: 42px; top: 245px; }
  .hotline {
    position: absolute; left: 6px; top: 258px;
    width: 162px; height: 48px;
    background: var(--ink);
    color: var(--alarm-yellow);
    font-size: 15.5px; line-height: 19px;
    padding: 6px 0 0 10px;
    transform: rotate(-7deg);
    transform-origin: left top;
    top: 265px;
  }
  .web {
    position: absolute; left: 12px; top: 314px;
    font-size: 10px; color: var(--ink);
    transform: rotate(-7deg);
    transform-origin: left top;
  }
  .brand {
    position: absolute; left: 0; top: 372px; width: 178px;
    text-align: center;
    color: var(--brand-green);
  }
  .brand-name { font-size: 30px; line-height: 34px; }
  .brand-line { font-size: 7px; letter-spacing: 1.2px; line-height: 12px; }
</style>
</head>
<body>
<div class="canvas">
  <section class="ad">
    <svg class="ad-field" viewBox="0 0 178 445" aria-hidden="true">
      <polygon points="0,0 178,0 178,317 0,339" fill="var(--alarm-yellow)"/>
    </svg>

    <h1 class="headline">WESPEN-<br>ALARM?</h1>

    <div class="wasp-art" role="img" aria-label="Illustration einer schwarz-gelben Wespe"></div>

    <div class="help-tag">WIR HELFEN!</div>
    <svg class="help-arrow" width="36" height="22" viewBox="0 0 36 22" aria-hidden="true">
      <polygon points="10,0 26,0 26,8 36,8 18,22 0,8 10,8" fill="var(--signal-red)"/>
    </svg>

    <div class="hotline">WESPENNOTRUF<br>(01234) 567 89 00</div>
    <div class="web">www.plagenfrei-team.example</div>

    <div class="brand">
      <div class="brand-name">Kessler</div>
      <div class="brand-line">SCHÄDLINGSBEKÄMPFUNG</div>
    </div>
  </section>
</div>
</body>
</html>
```